We need help creating industry specific one page marketing flyers

We are kicking off a campaign to target specific industry verticals and need help creating / designing one pager marketing collateral for each industry.

See attached our first industry, healthcare. I created this but want to make it more professional looking.

Here is our website (the website is old, we're refreshing this in the near future). www.brookvane.com

I want it in powerpoint format so that I can make adjustments to the one pager and create PDFs from it as well.

Target Market(s)

Property managers and facilities managers

Industry/Entity Type

Industry

Requirements
Must have
• Tie to our corporate logo colors
• Use plant pictures and visuals to tell the story
• Must be in an editable format (e.g. powerpoint) so I can make tweaks to the content

```html
<!DOCTYPE html>
<html lang="en">
<head>
<meta charset="utf-8">
<title>Brookvane – Indoor Plant Services for Healthcare Facilities</title>
<link href="https://fonts.googleapis.com/css2?family=Gelasio:wght@400&family=Questrial&display=swap" rel="stylesheet">
<style>
  :root {
    --leaf-green: #7aad3f;
    --panel-green: #7bab40;
    --slate-grey: #888888;
    --ink: #4e4e4e;
    --ink-dark: #1f1f1f;
    --paper: #ffffff;
    --divider: rgba(255,255,255,0.45);
  }
  * { box-sizing: border-box; margin: 0; padding: 0; }
  html, body { width: 960px; height: 1200px; overflow: hidden; background: var(--paper); }
  .flyer {
    position: relative; width: 960px; height: 1200px;
    background: var(--paper);
    font-family: "Questrial", "Century Gothic", sans-serif;
  }
  .serif { font-family: "Gelasio", Georgia, serif; font-weight: 400; }

  .brand {
    position: absolute; left: 45px; top: 112px;
    display: flex; align-items: center; gap: 14px;
  }
  .brand-name {
    font-family: "Gelasio", Georgia, serif; font-weight: 400;
    font-size: 76px; line-height: 1; color: var(--leaf-green);
  }
  .brand-mark {
    width: 22px; height: 22px; border-radius: 50%;
    background: var(--leaf-green);
  }

  .service-title {
    position: absolute; left: 549px; top: 64px; width: 380px;
    font-size: 30px; line-height: 36px; color: var(--leaf-green);
  }
  .intro {
    position: absolute; left: 45px; top: 246px; width: 380px;
    font-size: 29px; line-height: 37px; color: var(--ink);
  }

  .expertise {
    position: absolute; left: 38px; top: 391px; width: 374px; height: 346px;
    background: var(--panel-green); color: var(--paper);
    border-radius: 0 92px 0 100px;
    padding: 44px 24px 0 31px;
  }
  .expertise h2 { font-size: 30px; line-height: 37px; margin-bottom: 16px; }
  .expertise p { font-size: 16px; line-height: 24px; margin-bottom: 24px; }

  .photo { position: absolute; }
  .photo-lounge {
    left: 425px; top: 209px; width: 509px; height: 528px;
    border-radius: 120px 0 150px 0;
    background: linear-gradient(100deg, #4f7a2a 0%, #7ea53e 28%, #c9c79a 48%, #ece9dc 62%, #c8b245 78%, #8c7640 100%);
  }
  .photo-atrium {
    left: 126px; top: 750px; width: 288px; height: 300px;
    border-radius: 0 0 90px 0;
    background: linear-gradient(180deg, #7f8f9a 0%, #b7c1c3 30%, #d9d8cd 60%, #6f8f3c 85%, #4e7a2b 100%);
  }

  .benefits {
    position: absolute; left: 429px; top: 750px; width: 507px; height: 302px;
    background: var(--slate-grey); color: var(--paper);
    border-radius: 0 100px 0 90px;
    padding: 16px 48px 0 40px;
  }
  .benefits h2 { font-size: 28px; line-height: 36px; margin-bottom: 8px; }
  .benefit-list { list-style: none; }
  .benefit-list li {
    font-size: 16px; line-height: 24px;
    padding: 5px 0 6px;
    border-bottom: 1px solid var(--divider);
  }
  .benefit-list li:last-child { border-bottom: none; }

  .company-details {
    position: absolute; left: 41px; top: 1119px;
    font-size: 16px; line-height: 27px; color: var(--ink-dark);
  }
  .company-details .sep { padding: 0 14px; }
  .consultation {
    position: absolute; left: 490px; top: 1080px; width: 440px;
    font-size: 23px; line-height: 33px; color: var(--ink-dark);
  }
  .consultation .highlight { color: var(--leaf-green); }
</style>
</head>
<body>
<main class="flyer">
  <div class="brand">
    <span class="brand-name">Brookvane</span>
    <span class="brand-mark"></span>
  </div>

  <h1 class="service-title serif">Indoor Plant Design and Maintenance Services for Healthcare Facilities</h1>

  <p class="intro serif">We can help you make your healthcare facility more welcoming!</p>

  <section class="expertise">
    <h2 class="serif">We know healthcare facilities</h2>
    <p>We currently serve over 20 of the largest hospitals and healthcare facilities across the Bay Area</p>
    <p>We understand what works in a hospital from using the right moss to minimize dusty to the right plant</p>
  </section>

  <div class="photo photo-lounge" role="img" aria-label="Hospital lounge with a living green plant wall behind a long yellow sofa"></div>
  <div class="photo photo-atrium" role="img" aria-label="Glass-roofed atrium lined with potted trees in white planters"></div>

  <section class="benefits">
    <h2 class="serif">Benefits of plants...</h2>
    <ul class="benefit-list">
      <li>High impact amenity at a low cost</li>
      <li>Create a calming environment for patients</li>
      <li>Patients’ stress levels increase in the hospital, however exposure to natural settings has the ability to reduce stress and enhance the process of healing</li>
      <li>Are proven to provide health benefits such as cleaning indoor air</li>
    </ul>
  </section>

  <address class="company-details" style="font-style:normal">
    Brookvane, Inc. PO Box 41870 Larkfield, CA 94999<br>
    info@brookvane.com<span class="sep">|</span>www.brookvane.com
  </address>

  <p class="consultation serif">For a design consultation, please contact <span class="highlight">555-014-2290</span> or Dana Whitlock at <span class="highlight">whitlock@brookvane.com</span></p>
</main>
</body>
</html>
```